Online Marketplace Startup for Community Facilities (Tovaroom)

A innovative, modern website design is required for a new startup called Tovaroom. Tovaroom will be an online marketplace for searching for and booking community facilities, such as schools facilities (sports grounds, halls, classrooms etc.), churches, hospitals and other community facilities.

The attached brief has been created to provide guidance on the structure and content required.

The web design shall feature a modern, innovative but user friendly interface similar style to other web start up pages:
www.hallquiver.co.uk
www.vendlark.com.au
www.artfennel.com.au

The web design shall be ‘wordpress’ compliant and allow for future functionality to be added and coded (e.g. animations, flash, blogs etc) and content to be editable.

The following brief has been created to provide guidance on the structure and content required.

An existing logo developed for Tovaroom shall be utilised and incorporated in the top left hand cover of the cover landing page (refer to attached logo designs).

Refer to attached 'Website brief' for more details on requirements.
Updates

Project Deadline Extended
Reason: I wish to grant an extension to the deadline to provide designers with more time to submit their designs.

Target Market(s)

TovaRoom will focus on building a customer network of both community facility owners (schools, hospitals, churches) and hirers (non-government organisations, community groups, event management companies, commercial businesses). Members of the general public will also be encouraged to book facilities for private functions.

Industry/Entity Type

Community

Coding

Coded - Design and coding required

Number of Pages Required

5+ page

Font styles to use
Sans Serif

Colors
3176b5
ffffff
85cae6
33a6d7

Requirements
Must have
• The web design shall feature a modern, innovative but user friendly interface similar style to other web start up pages:
• www.hallquiver.co.uk
• www.vendlark.com.au
• www.artfennel.com.au
• The web design shall be ‘wordpress’ compliant and allow for future functionality to be added and coded (e.g. animations, flash, blogs etc) and content to be editable.
• Refer to Project brief for other requirements
Nice to have
• Refer to Project brief
Should not have
• Refer to Project brief

```html
<!DOCTYPE html>
<html lang="en">
<head>
<meta charset="utf-8">
<title>Tovaroom</title>
<link href="https://fonts.googleapis.com/css2?family=Raleway:wght@300;400;500;600;700&display=swap" rel="stylesheet">
<style>
:root{
  --brand-blue:#2f6bc4;
  --accent:#33a6d7;
  --navy:#1f3f7a;
  --ink:#3a3a3a;
  --body:#555;
  --dark:#636469;
  --white:#fff;
  --field-text:#9a9a9a;
}
*{box-sizing:border-box;margin:0;padding:0}
html,body{width:918px;height:1200px;overflow:hidden;background:var(--white);font-family:'Raleway',sans-serif}
.page{position:relative;width:918px;height:1200px}
.abs{position:absolute}
.hero{left:0;top:0;width:918px;height:368px;background:var(--brand-blue)}
.brand{left:103px;top:14px;display:flex;align-items:center;gap:7px;color:var(--white);font-size:21px;font-weight:500}
.brand .dot{width:20px;height:20px;border-radius:50%;background:var(--white)}
.nav{top:23px;left:522px;display:flex;gap:0;font-size:8px;color:var(--white)}
.nav a{color:inherit;text-decoration:none;position:absolute;white-space:nowrap}
.social{display:flex;gap:5px}
.social span{width:7px;height:7px;border-radius:50%;background:currentColor;display:block}
.hero-social{left:781px;top:26px;color:var(--white)}
.headline{left:0;width:962px;top:101px;text-align:center;color:var(--white);font-size:17px;font-weight:300;line-height:21px}
.devices{left:222px;top:182px;width:430px;height:236px;border-radius:8px;background:linear-gradient(180deg,#2a2a2a 0%,#e9edf2 8%,#f4f6f8 70%,#cfd3d8 100%)}
.service{width:170px;text-align:center;top:482px}
.service .badge{width:64px;height:64px;border-radius:50%;background:var(--accent);margin:0 auto;display:flex;align-items:center;justify-content:center}
.service p{margin-top:16px;font-size:7.5px;color:var(--navy)}
.office-art{left:103px;top:646px;width:259px;height:192px;background:linear-gradient(180deg,#ffffff 0%,#f3d6c4 40%,#d4d6da 75%,#555 100%)}
.about{left:394px;top:646px;width:410px}
.about h2{font-size:13.5px;font-weight:700;color:var(--ink);line-height:17px}
.about .rule{width:46px;height:1px;background:var(--ink);margin:12px 0 16px 1px}
.about p{font-size:7.2px;line-height:9px;color:var(--body)}
.features{display:flex;gap:45px;margin-top:22px}
.feature{width:180px}
.feature h3{font-size:9px;font-weight:600;color:var(--ink);display:flex;align-items:center;gap:8px;margin-bottom:8px}
.contact{left:0;top:838px;width:918px;height:320px;background:var(--dark)}
.contact h2{position:absolute;left:113px;top:52px;font-size:21px;font-weight:400;color:var(--white)}
.contact .intro{position:absolute;left:113px;top:88px;width:320px;font-size:7.5px;line-height:9.8px;color:var(--white)}
.info{position:absolute;left:115px;display:flex;gap:10px;font-size:7.5px;line-height:9.5px;color:var(--white)}
.info svg{flex:none;width:14px}
.field{position:absolute;left:489px;width:301px;height:26px;background:var(--white);border-radius:4px;font-size:7px;color:var(--field-text);padding:9px 16px}
.submit{position:absolute;left:489px;top:255px;width:57px;height:26px;border-radius:4px;background:var(--accent);color:var(--white);font-size:7.5px;text-align:center;line-height:26px}
.footer{left:0;top:1158px;width:918px;height:42px}
.footer .copy{position:absolute;left:104px;top:17px;font-size:7px;color:var(--body)}
.footer .nav{top:17px;left:350px;color:var(--ink);font-size:7.5px}
.footer-social{left:781px;top:18px;color:var(--ink)}
</style>
</head>
<body>
<div class="page">
  <header class="abs hero">
    <div class="abs brand"><span class="dot"></span>TovaRoom</div>
    <nav class="abs nav" style="left:0">
      <a style="left:522px">Home</a>
      <a style="left:563px">About</a>
      <a style="left:598px">Services</a>
      <a style="left:645px">News &amp; Updates</a>
      <a style="left:720px">Contact</a>
    </nav>
    <div class="abs social hero-social"><span></span><span></span><span></span></div>
    <h1 class="abs headline">Utilising your facility to create value<br>for your organisation and the community</h1>
  </header>

  <div class="abs devices" role="img" aria-label="Laptop and phone showing the facility dashboard with charts"></div>

  <section>
    <div class="abs service" style="left:103px">
      <div class="badge"><svg width="26" height="22" viewBox="0 0 26 22" fill="none" stroke="#fff" stroke-width="1.6"><path d="M3 8h5l10-6v18L8 14H3z"/><path d="M7 14l2 6h3l-2-6"/></svg></div>
      <p>Marketing and Promotion of your facility</p>
    </div>
    <div class="abs service" style="left:285px">
      <div class="badge"><svg width="28" height="20" viewBox="0 0 28 20" fill="none" stroke="#fff" stroke-width="1.6"><rect x="5" y="2" width="18" height="12" rx="1"/><path d="M2 17h24"/></svg></div>
      <p>Administer bookings and enquiries</p>
    </div>
    <div class="abs service" style="left:461px">
      <div class="badge"><svg width="26" height="20" viewBox="0 0 26 20" fill="none" stroke="#fff" stroke-width="1.6"><rect x="2" y="3" width="22" height="15" rx="2"/><path d="M15 8h9v6h-9z"/></svg></div>
      <p>Invoicing and Payment collection</p>
    </div>
    <div class="abs service" style="left:641px">
      <div class="badge"><svg width="24" height="22" viewBox="0 0 24 22" fill="none" stroke="#fff" stroke-width="1.6"><rect x="2" y="12" width="5" height="8"/><rect x="9.5" y="7" width="5" height="13"/><rect x="17" y="2" width="5" height="18"/></svg></div>
      <p>Bookings reports and customer service</p>
    </div>
  </section>

  <div class="abs office-art" role="img" aria-label="Illustration of a woman working on a laptop at a desk with a plant and a cup"></div>

  <section class="abs about">
    <h2>We provide a cloud based online solution for managing your facility.</h2>
    <div class="rule"></div>
    <p>Consectetuer adipiscing elit. Aenean commodo ligula eget dolor. Aenean massa. Cum sociis natoque penatibus et magnisdis parturient montes, nascetur ridiculus mus.Donec quam felis, ultricies nec, pellentesque eu, pretium quis, sem. Nulla consequat massa quis enim. ridiculus mus.Donec quam felis, ultricies nec, pe.</p>
    <div class="features">
      <div class="feature">
        <h3><svg width="10" height="7" viewBox="0 0 10 7"><path d="M2.5 7a2.5 2.5 0 0 1 0-5 3 3 0 0 1 5.6.5A2.3 2.3 0 0 1 8 7z" fill="#3a3a3a"/></svg>Donec quam felis</h3>
        <p>Lorem ipsum dolor sit amet, consectetuer adipiscing elit. Aenean commodo ligula eget dolor.</p>
      </div>
      <div class="feature">
        <h3><svg width="8" height="9" viewBox="0 0 8 9" fill="#3a3a3a"><ellipse cx="4" cy="1.5" rx="4" ry="1.5"/><rect x="0" y="2.5" width="8" height="2" rx="1"/><rect x="0" y="5" width="8" height="2" rx="1"/><rect x="0" y="7" width="8" height="2" rx="1"/></svg>Donec quam felis</h3>
        <p>Lorem ipsum dolor sit amet, consectetuer adipiscing elit. Aenean commodo ligula eget dolor.</p>
      </div>
    </div>
  </section>

  <section class="abs contact">
    <h2>Contact Us</h2>
    <p class="intro">We are here to assist you by phone, email or via our social media channels.<br>Use the simple form on this page to send us a message, or feel free to contact us using the information provided below.</p>
    <div class="info" style="top:145px"><svg viewBox="0 0 14 14" height="14"><path d="M7 1a4 4 0 0 1 4 4c0 3-4 8-4 8S3 8 3 5a4 4 0 0 1 4-4z" fill="#fff"/><circle cx="7" cy="5" r="1.5" fill="#636469"/></svg><span>48 Larkfield Rd, #210<br>Portland, OR 972</span></div>
    <div class="info" style="top:176px"><svg viewBox="0 0 14 14" height="12"><path d="M3 1l3 3-1.5 2a8 8 0 0 0 4 4L10.5 8.5l3 3-2 2C6 13 1 8 1 3z" fill="#fff"/></svg><span>(555) 014-2270</span></div>
    <div class="info" style="top:204px"><svg viewBox="0 0 14 10" height="10"><rect width="14" height="10" rx="1" fill="#fff"/><path d="M0.5 0.8L7 6l6.5-5.2" fill="none" stroke="#636469" stroke-width="1"/></svg><span>info@tovaroom.com</span></div>

    <div class="field" style="top:52px">Full Name</div>
    <div class="field" style="top:86px">Email</div>
    <div class="field" style="top:120px">Subject</div>
    <div class="field" style="top:155px;height:89px">Message</div>
    <div class="submit">Submit</div>
  </section>

  <footer class="abs footer">
    <span class="copy">© 2017 Tovaroom Pty. Ltd.</span>
    <nav class="abs nav" style="left:0">
      <a style="left:350px">Home</a>
      <a style="left:388px">About</a>
      <a style="left:426px">Services</a>
      <a style="left:473px">News &amp; Updates</a>
      <a style="left:547px">Contact</a>
    </nav>
    <div class="abs social footer-social"><span></span><span></span><span></span></div>
  </footer>
</div>
</body>
</html>
```